Coverneugestaltung einer Zeitschrift für Betroffene mit Allergien
Zielgruppe
Wir sind ein medizinischer Verlag und geben Patientenzeitschriften heraus. Das Magazin 'Pollenta' richtet sich an Betroffene mit Allergien, Nahrungsmittelunverträglichkeiten, Lungen- und Hauterkrankungen
Aufgabenstellung
Das Cover sollte modern und seriös wirken. Die rote Ecke unten rechts "Ihr Exemplar zum Mitnehmen" muss zwingend unten rechts übernommen werden. Die Covergestaltung sollte so sein, dass zukünftig verschiedene Titelbilder verwendet werden können (u.a. Freisteller). Die Zeitschrift "Pollenta" erscheint viermal im Jahr.
Es darf alles verändert werden, Schrift, Farbe, Wort-Bild-Marke etc. Wir sind hier offen für Neues.

```html
<!DOCTYPE html>
<html lang="de">
<head>
<meta charset="utf-8">
<title>Pollenta – Cover</title>
<link href="https://fonts.googleapis.com/css2?family=Fira+Sans:wght@400;600;700&display=swap" rel="stylesheet">
<style>
  :root {
    --page-bg: #e4e4e4;
    --teal: #1fa3a6;
    --white: #ffffff;
    --ink: #4a5458;
    --photo-warm: #c89a78;
    --photo-hair: #6b4632;
    --photo-light: #e9d7c8;
    --photo-blue: #5b78b8;
  }
  * { margin: 0; padding: 0; box-sizing: border-box; }
  html, body {
    width: 1200px; height: 900px; overflow: hidden;
    background: var(--page-bg);
    font-family: "Fira Sans", Arial, sans-serif;
  }
  .cover {
    position: absolute; left: 303px; top: 30px;
    width: 594px; height: 840px;
    background: var(--white);
    box-shadow: 0 6px 18px rgba(0,0,0,.18);
    overflow: hidden;
  }
  .cover-shapes { position: absolute; inset: 0; }
  .issue {
    position: absolute; right: 22px; top: 14px;
    font-size: 10px; color: var(--white); opacity: .85;
  }
  .masthead {
    position: absolute; left: 44px; top: 44px;
    transform: rotate(-9deg); transform-origin: left top;
    color: var(--white);
  }
  .masthead-name {
    font-size: 74px; font-weight: 600; line-height: 1; letter-spacing: -1px;
  }
  .masthead-tagline {
    font-size: 15px; font-weight: 400; margin-top: 6px; opacity: .95;
  }
  .lead-story {
    position: absolute; right: 40px; top: 505px;
    transform: rotate(-18deg); text-align: right;
  }
  .lead-title { font-size: 28px; font-weight: 700; color: var(--teal); line-height: 1.1; }
  .lead-sub { font-size: 15px; color: var(--ink); margin-top: 2px; }
  .teaser {
    position: absolute; color: var(--white);
    transform: rotate(-12deg); transform-origin: left top;
  }
  .teaser-title { font-size: 19px; font-weight: 700; line-height: 1.1; }
  .teaser-sub { font-size: 12.5px; line-height: 1.28; margin-top: 3px; opacity: .95; }
  .teaser--research { left: 30px; top: 752px; }
  .teaser--cold { left: 285px; top: 645px; }
  .takeaway-badge {
    position: absolute; left: 480px; top: 560px;
    width: 96px; height: 96px; border-radius: 50%;
    background: var(--white);
    display: flex; align-items: center; justify-content: center;
    text-align: center;
    font-size: 10px; font-weight: 600; line-height: 1.25; color: var(--teal);
  }
  .takeaway-badge span { transform: rotate(-12deg); display: block; }
</style>
</head>
<body>
  <main class="cover">
    <svg class="cover-shapes" viewBox="0 0 594 840" width="594" height="840">
      <defs>
        <radialGradient id="photoTones" cx="50%" cy="50%" r="65%">
          <stop offset="0%" stop-color="#e9d7c8"/>
          <stop offset="35%" stop-color="#c89a78"/>
          <stop offset="65%" stop-color="#6b4632"/>
          <stop offset="85%" stop-color="#5b78b8"/>
          <stop offset="100%" stop-color="#9a9a9a"/>
        </radialGradient>
      </defs>
      <rect class="cover-photo" x="0" y="130" width="594" height="620" fill="url(#photoTones)"
            role="img" aria-label="Titelfoto: fünf lachende junge Leute liegen im Kreis, Köpfe zusammen, Daumen hoch"/>
      <path class="top-band-edge" d="M0 0 H594 V150 C420 165 180 215 0 285 Z" fill="var(--white)"/>
      <path class="top-band" d="M0 0 H594 V136 C420 150 180 200 0 268 Z" fill="var(--teal)"/>
      <path class="lower-band" d="M0 700 C200 630 420 520 594 440 V840 H0 Z" fill="var(--white)"/>
      <path class="footer-band" d="M0 740 C200 670 420 570 594 510 V840 H0 Z" fill="var(--teal)"/>
    </svg>

    <div class="issue">Ausgabe 01/17</div>

    <header class="masthead">
      <div class="masthead-name">pollenta</div>
      <div class="masthead-tagline">Ihr Fachmagazin für Allergien, Haut und Lunge</div>
    </header>

    <section class="lead-story">
      <h1 class="lead-title">Glücklich im Alter</h1>
      <p class="lead-sub">Den Lebensmut wiederfinden</p>
    </section>

    <article class="teaser teaser--research">
      <h2 class="teaser-title">Neue Hoffnung<br>in der Forschung</h2>
      <p class="teaser-sub">Wie Stammzellen Ihr<br>Leben verändern</p>
    </article>

    <article class="teaser teaser--cold">
      <h2 class="teaser-title">Ein Schnupfen-<br>viele Ursachen</h2>
      <p class="teaser-sub">Unter welcher Art leiden Sie?</p>
    </article>

    <div class="takeaway-badge"><span>Ihr Exemplar<br>zum Mitnehmen</span></div>
  </main>
</body>
</html>
```